Structural Engineering Business Card

Orvik Drafting does residential house plans for clients in Central Florida. Would like simple but elegant business card that is appropriate for a house plan engineering company. Prefer black business card with black/white them but open to other shades of blue. I uploaded a sample card that I came across that looked good but please come up with your own creative designs.

Contact Information for Business Card

Name, Title, Phone, Email, Address, website

```html
<!DOCTYPE html>
<html lang="en">
<head>
<meta charset="utf-8">
<title>Orvik Drafting – Business Card</title>
<link rel="stylesheet" href="https://fonts.googleapis.com/css2?family=Fira+Sans:wght@400;700;800&display=swap">
<style>
  :root {
    --backdrop: #8a8a8e;
    --backdrop-edge: #5e5e62;
    --card-blue: #2e2580;
    --card-blue-deep: #241d6a;
    --drawing-light: #5a52a8;
    --ink-white: #ffffff;
    --ink-soft: #e6e4f4;
  }
  * { margin: 0; padding: 0; box-sizing: border-box; }
  html, body {
    width: 1200px; height: 781px; overflow: hidden;
  }
  body {
    background: radial-gradient(ellipse at 50% 45%, var(--backdrop) 0%, var(--backdrop-edge) 100%);
    font-family: "Fira Sans", sans-serif;
    position: relative;
  }
  .card {
    position: absolute;
    top: 240px;
    width: 520px;
    height: 300px;
    border-radius: 22px;
    background: linear-gradient(160deg, var(--card-blue) 0%, var(--card-blue-deep) 100%);
    box-shadow: 0 18px 40px rgba(0,0,0,.35);
    overflow: hidden;
    color: var(--ink-white);
  }
  .card--contact { left: 50px; }
  .card--brand { left: 630px; }

  .blueprint-area {
    position: absolute;
    border-radius: 8px;
  }
  .card--contact .blueprint-area {
    left: 250px; top: 50px; width: 250px; height: 230px;
    background: radial-gradient(ellipse at 50% 55%, var(--drawing-light) 0%, rgba(90,82,168,0) 72%);
  }
  .card--brand .blueprint-area {
    left: 20px; top: 20px; width: 480px; height: 260px;
    background: radial-gradient(ellipse at 50% 55%, var(--drawing-light) 0%, rgba(90,82,168,0) 75%);
  }

  .holder { position: absolute; left: 34px; top: 30px; }
  .holder__name { font-weight: 700; font-size: 22px; letter-spacing: .5px; }
  .holder__title { font-size: 12px; color: var(--ink-soft); margin-top: 2px; }

  .company-name--small {
    position: absolute; left: 34px; top: 96px;
    font-weight: 800; font-size: 19px;
  }
  .address {
    position: absolute; left: 34px; top: 128px;
    font-size: 13px; line-height: 17px; color: var(--ink-soft);
  }
  .contact-list {
    position: absolute; left: 34px; top: 172px;
    list-style: none; font-size: 14px; line-height: 22px; color: var(--ink-soft);
  }
  .contact-list li { display: flex; align-items: center; gap: 7px; }
  .contact-list svg { width: 12px; height: 12px; flex: none; }

  .company-name--large {
    position: absolute; left: 0; right: 0; top: 112px;
    text-align: center;
    font-weight: 800; font-size: 54px; letter-spacing: -.5px;
  }
</style>
</head>
<body>

  <section class="card card--contact">
    <div class="blueprint-area" role="img" aria-label="Blueprint elevation drawing of a gabled house"></div>
    <div class="holder">
      <div class="holder__name">MARCUS DALE</div>
      <div class="holder__title">Manager</div>
    </div>
    <div class="company-name--small">Orvik Drafting</div>
    <div class="address">418 Lakeview Road Ste 2<br>Clermont, FL 34711</div>
    <ul class="contact-list">
      <li>
        <svg viewBox="0 0 12 12" fill="none" stroke="currentColor" stroke-width="1.2"><rect x="3" y="0.8" width="6" height="10.4" rx="1"/><line x1="5" y1="9.3" x2="7" y2="9.3"/></svg>
        407-555-0182
      </li>
      <li>
        <svg viewBox="0 0 12 12" fill="none" stroke="currentColor" stroke-width="1.2"><path d="M2 1.5h2.3l1 2.6-1.4 1a6 6 0 0 0 3 3l1-1.4 2.6 1V10a1 1 0 0 1-1 1A9 9 0 0 1 1 2.5a1 1 0 0 1 1-1z"/></svg>
        407-555-0147
      </li>
      <li>
        <svg viewBox="0 0 12 12" fill="none" stroke="currentColor" stroke-width="1.2"><rect x="0.8" y="2.3" width="10.4" height="7.4" rx="1"/><path d="M1 3l5 3.8L11 3"/></svg>
        info@orvikdrafting.com
      </li>
      <li>
        <svg viewBox="0 0 12 12" fill="none" stroke="currentColor" stroke-width="1.1"><circle cx="6" cy="6" r="5.2"/><ellipse cx="6" cy="6" rx="2.3" ry="5.2"/><line x1="0.8" y1="6" x2="11.2" y2="6"/></svg>
        orvikdrafting.com
      </li>
    </ul>
  </section>

  <section class="card card--brand">
    <div class="blueprint-area" role="img" aria-label="Blueprint floor plans and roof section drawings"></div>
    <div class="company-name--large">Orvik Drafting</div>
  </section>

</body>
</html>
```